Wellness Thai Massage Geschäft benötigt eine Preis/Info Broschüre

Ein kleines Thai Massage Geschäft in Bayern: Kolavan Thaimassage
Benötigt eine kleine Preisliste, sowie eine kurze Beschreibung vom Unternehmen. Angeboten werden traditionelle Thaimassagen. Der Farbstil soll dem Logo (Anhang) angepasst sein. Alle Bilder außer die Bilder von der Geschäftsführerin sind optional zur Verwendung verfügbar. Mehr Info wie Preise, etc. sind verfügbar auf der Website https://www.kolavanthaimassage.example/

```html
<!DOCTYPE html>
<html lang="de">
<head>
<meta charset="utf-8">
<title>Kolavan Thaimassage – Flyer</title>
<link rel="stylesheet" href="https://fonts.googleapis.com/css2?family=Comfortaa:wght@300;400&family=Montserrat:ital,wght@0,300;0,400;0,500;0,600;1,300&display=swap">
<style>
:root{
  --stage:#ececee;
  --maroon:#7a1824;
  --maroon-deep:#5e0f19;
  --crimson:#a3293b;
  --crimson-low:#8c1f2f;
  --rose:#d98a92;
  --rose-pale:#f0c9cc;
  --gold:#f2b23f;
  --cream:#f7e0b5;
  --ink-light:#fff6f4;
  --price:#f3a9a4;
}
*{margin:0;padding:0;box-sizing:border-box}
html,body{width:1200px;height:838px;overflow:hidden;background:var(--stage)}
body{position:relative;font-family:"Montserrat",sans-serif;color:var(--ink-light)}
.page{position:absolute;top:63px;width:506px;height:715px;overflow:hidden;background:linear-gradient(180deg,var(--crimson) 40%,var(--crimson-low));box-shadow:3px 4px 8px rgba(0,0,0,.35)}
.page--info{left:75px}
.page--prices{left:619px}
.layer{position:absolute;inset:0;width:506px;height:715px}
.photo{position:absolute}
.photo--massage{left:0;top:0;width:506px;height:380px;background:radial-gradient(ellipse at 65% 45%,#e7b58f 0%,#b97a55 35%,#6e3a26 70%,#3c1d14 100%)}
.photo--stones{left:0;top:0;width:506px;height:300px;background:radial-gradient(circle at 82% 35%,#3a3532 0%,#26211f 22%,#6b4a33 45%,#3d2417 70%,var(--maroon-deep) 100%)}
.bubble{position:absolute;border-radius:50%;border:5px solid rgba(240,201,204,.75);box-shadow:0 0 0 3px rgba(163,41,59,.4)}
.brand{position:absolute;display:flex;align-items:center;gap:14px}
.brand__mark{background:#fbf1c8;border:1px solid var(--rose-pale)}
.brand__name{font-variant:small-caps;color:var(--cream);font-weight:500;letter-spacing:1.5px;line-height:1.3}
.page--info .brand{left:8px;top:13px}
.page--info .brand__mark{width:60px;height:41px}
.page--info .brand__name{font-size:17px;margin-left:7px}
.page--prices .brand{left:21px;top:20px}
.page--prices .brand__mark{width:69px;height:49px}
.page--prices .brand__name{font-size:21px;margin-left:14px}
.heading{position:absolute;font-family:"Comfortaa",sans-serif;font-weight:300;color:var(--gold);font-size:21px}
.body-text{position:absolute;font-size:10.6px;line-height:14.4px;font-weight:400}
.note{position:absolute;font-style:italic;font-weight:300;font-size:9.4px;line-height:13px;color:var(--rose-pale)}
.contact{position:absolute;right:13px;text-align:right;color:var(--ink-light)}
.contact__name{font-family:"Comfortaa",sans-serif;font-size:16.5px;color:var(--maroon);line-height:18px}
.contact__web{font-size:11.5px;color:var(--maroon);line-height:16px}
.contact__line{font-size:7.6px;line-height:12px;font-weight:500}
.contact__line svg{vertical-align:-1px}
.title{position:absolute;left:21px;top:104px;font-family:"Comfortaa",sans-serif;font-weight:300;font-size:22px;line-height:29px;color:#fff}
.service{position:absolute;width:219px}
.service__title{font-family:"Comfortaa",sans-serif;font-size:12.6px;line-height:13px;color:var(--gold);padding-left:33px;position:relative;min-height:20px}
.service__title::before{content:"";position:absolute;left:2px;top:0;width:22px;height:22px;border-radius:50%;background:var(--rose-pale)}
.service__text{font-size:9.3px;line-height:10.2px;text-align:justify;margin-top:5px}
.service__price{font-size:8.8px;line-height:11px;font-weight:600;color:var(--price);margin-top:13px}
</style>
</head>
<body>

<section class="page page--info">
  <div class="photo photo--massage" role="img" aria-label="Foto: Schultermassage auf einer Liege mit Handtuch"></div>
  <svg class="layer" viewBox="0 0 506 715" aria-hidden="true">
    <path d="M0 0H240C225 60 150 95 0 98Z" fill="var(--maroon)"/>
    <path d="M0 330C120 375 250 415 506 335V715H0Z" fill="var(--rose)" opacity=".85"/>
    <path d="M0 340C120 385 250 425 506 348V715H0Z" fill="var(--crimson)"/>
    <path d="M290 715C330 660 410 635 506 625V715Z" fill="var(--rose)"/>
  </svg>
  <div class="bubble" role="img" aria-label="Foto: Buddha-Statue mit roten Blüten" style="left:11px;top:178px;width:142px;height:142px;background:radial-gradient(circle,#8a5a3a,#5a2e1f 60%,#a33d3a)"></div>
  <div class="bubble" role="img" aria-label="Foto: Massageöle und Hot Stones" style="left:141px;top:196px;width:128px;height:128px;background:radial-gradient(circle,#e9e3d6,#2b2d45 55%,#b07f54)"></div>
  <div class="brand"><span class="brand__mark"></span><span class="brand__name">Kolavan<br>Thaimassage</span></div>

  <h2 class="heading" style="left:28px;top:375px">Was ist Thai Massage eigentlich?</h2>
  <p class="body-text" style="left:25px;top:405px;width:463px;text-align:justify">Thai Massage existiert schon seit ca. über 2500 Jahren welches sich im Laufe der Zeit zu einer effektiven Methode gegen Schmerzzustände und auch Krankheiten entwickelt welches in der heutigen Zeit sogar Kultstatus erreicht hat. Diese thailändische Heilungsmethode verlangt eine professionelle Ausbildung die Hintergrundwissen und langes Training mit sich bringt.</p>
  <h2 class="heading" style="left:28px;top:503px;font-size:22px">Über uns</h2>
  <p class="body-text" style="left:25px;top:532px;width:463px">Kolavan Thaimasage legt einen hohen Wert auf die Zufriedenheit und das Wohlbefinden von jedem Kunden. Wenn sie also z.B nach viel Arbeit gestresst sind und Schmerzen an einer bestimmten Region aufgebaut haben, dann sind sie bei uns an der richtigen Adresse. Geführt wird das Massagestudio von Malee Sommer, die professionell ausgebildet wurde und auch beruflich schon in Deutschland sowie in Thailand viel Erfahrung gesammelt hat. Wir freuen uns schon auf Ihren Besuch bei Kolavan Thaimassage!</p>
  <p class="note" style="left:25px;top:677px">Bitte erkundigen sie sich hierfür im Geschäft um<br>über ein erweitertes Angebot zu erfahren.</p>
  <div class="contact" style="top:644px">
    <div class="contact__name">Kolavan Thaimassage</div>
    <div class="contact__web">www.kolavanthaimassage.example</div>
    <div class="contact__line"><svg width="8" height="8" viewBox="0 0 10 10"><circle cx="5" cy="5" r="4.2" fill="none" stroke="currentColor"/><path d="M3.5 3l1 1-0.6 .8 1.5 1.5.8-.6 1 1-.8.8c-1.5 0-3.5-2-3.5-3.5z" fill="currentColor"/></svg> 0170 5550123 &nbsp;<svg width="8" height="7" viewBox="0 0 10 8"><rect x=".5" y=".5" width="9" height="7" fill="none" stroke="currentColor"/><path d="M.5 .5 5 4.5 9.5 .5" fill="none" stroke="currentColor"/></svg> info@kolavan-thaimassage.example</div>
    <div class="contact__line">Seeweg 14 , 83600 Musterau, Deutschland</div>
  </div>
</section>

<section class="page page--prices">
  <div class="photo photo--stones" role="img" aria-label="Foto: gestapelte schwarze Hot Stones mit Kerzen"></div>
  <svg class="layer" viewBox="0 0 506 715" aria-hidden="true">
    <path d="M0 0H300C330 90 300 200 0 240Z" fill="var(--maroon)" opacity=".75"/>
    <path d="M0 218C150 300 330 300 506 240V715H0Z" fill="var(--rose)" opacity=".85"/>
    <path d="M0 240C150 318 340 310 506 262V715H0Z" fill="var(--crimson)"/>
    <path d="M290 715C330 660 410 635 506 625V715Z" fill="var(--rose)"/>
  </svg>
  <div class="bubble" role="img" aria-label="Foto: Hot Stones und Öle" style="left:22px;top:167px;width:84px;height:84px;background:radial-gradient(circle,#3c3a3c,#6b4e39 65%,#c08a5a)"></div>
  <div class="bubble" role="img" aria-label="Foto: Massageraum mit Liege" style="left:103px;top:167px;width:84px;height:84px;background:radial-gradient(circle,#7c2b2e,#b06044 60%,#e3c59c)"></div>
  <div class="bubble" role="img" aria-label="Foto: Massageöle und Steine" style="left:185px;top:167px;width:84px;height:84px;background:radial-gradient(circle,#d6c7a8,#2e2c3a 55%,#9c6b44)"></div>
  <div class="brand"><span class="brand__mark"></span><span class="brand__name">Kolavan<br>Thaimassage</span></div>
  <h1 class="title">Thailändische<br>Heilungsmethode verlangt</h1>

  <article class="service" style="left:22px;top:275px">
    <h3 class="service__title">Traditionelle<br>Thai-Sport Massage</h3>
    <p class="service__text">Mt der traditionellen Thai-Massage werden durch Akupressur, Dehnung und Energielinien-Massage Energieblockaden gelöst. Es wird an 10 Energiepunkten und Linien massiert, die für den Einklang von Körper und Geist wichtig sind. Somit wird eine innere Balance und der Fluss der Lebensenergie erreicht</p>
    <p class="service__price">60 Minuten= 54 Euro<br>90 Minuten= 76 Euro</p>
  </article>
  <article class="service" style="left:22px;top:444px">
    <h3 class="service__title">Aromaöl Massage</h3>
    <p class="service__text">Die Aromaöl Massage ist eine Behandlungsform zur Regeneration und Harmonisierung des gesamten Körpers. Dabei wird das Basisöl mit ätherischen Ölen angereichert. Die Aromatherapie kann anregend oder entspannend abgestimmt werden</p>
    <p class="service__price">60 Minuten= 51 Euro<br>90 Minuten= 72 Euro</p>
  </article>
  <article class="service" style="left:22px;top:584px">
    <h3 class="service__title">Hot Stone Massage</h3>
    <p class="service__text">Bei der Hot Stone Massage werden angewärmte Vulkansteine entlag der Energielinien angebracht. Durch die abgegebene gespeicherte Wärme wird der Energiefluss und die Blutzirkulation gesteigert. Es kommt im ganzen Körper zu einer Tiefenentspannung</p>
    <p class="service__price">90 Minuten = 83 Euro</p>
  </article>
  <article class="service" style="left:270px;top:275px">
    <h3 class="service__title">Fussreflexzonen<br>Massage</h3>
    <p class="service__text">Eine Massage für den wohl für den strapaziertesten Körperteil, den Füssen, setzt neue Kräfte frei und verleiht Vitalität</p>
    <p class="service__price">30 Minuten = 35 Euro<br>60 Minuten = 62 Euro</p>
  </article>
  <article class="service" style="left:270px;top:405px">
    <h3 class="service__title">Rücken-Thai Massage</h3>
    <p class="service__text">Bei dieser Massagetechnik wird größtenteils der Rücken sowie auch Nacken, Hinterkopf, Schulter und Finger involviert. Diese Massage eignet sich besonders falls eines dieser Bereiche verspannt oder Schmerzen verursacht.</p>
    <p class="service__price">30 Minuten = 35 Euro<br>60 Minuten = 72 Euro</p>
  </article>
  <p class="note" style="left:268px;top:534px">Bitte erkundigen sie sich hierfür im Geschäft um<br>über ein erweitertes Angebot zu erfahren.</p>

  <div class="contact" style="top:644px">
    <div class="contact__name">Kolavan Thaimassage</div>
    <div class="contact__web">www.kolavanthaimassage.example</div>
    <div class="contact__line"><svg width="8" height="8" viewBox="0 0 10 10"><circle cx="5" cy="5" r="4.2" fill="none" stroke="currentColor"/><path d="M3.5 3l1 1-0.6 .8 1.5 1.5.8-.6 1 1-.8.8c-1.5 0-3.5-2-3.5-3.5z" fill="currentColor"/></svg> 0170 5550123 &nbsp;<svg width="8" height="7" viewBox="0 0 10 8"><rect x=".5" y=".5" width="9" height="7" fill="none" stroke="currentColor"/><path d="M.5 .5 5 4.5 9.5 .5" fill="none" stroke="currentColor"/></svg> info@kolavan-thaimassage.example</div>
    <div class="contact__line">Seeweg 14 , 83600 Musterau, Deutschland</div>
  </div>
</section>

</body>
</html>
```